Quarrytide Hosting - Direct Mailer / Flyer

We are excited to announce the launch of our new company, Quarrytide Hosting, a premier cohosting facility and data center dedicated to Cryptocurrency Miners. Our website, https://quarrytidehosting.example, provides detailed information about our offerings and showcases the innovative design schemes for the entire project.

Quarrytide Hosting stands out in the industry by offering both GPU Hosting and ASIC Hosting services in our state-of-the-art facility, equipped with an impressive 17 Megawatts of available power. What sets us apart is our unique billing system based on actual metered power usage. We charge $0.08 for ASIC miners and $0.09 for GPU miners, ensuring cost-effectiveness and transparency for our clients.

Our commitment to excellence is evident in our use of cutting-edge technology, top-notch facilities, and strategic partnerships. These elements come together to deliver exceptional solutions tailored for real-world applications in the cryptocurrency space.

As part of our promotional efforts, we are developing a direct mailer/flyer to introduce Quarrytide Hosting to a wider audience. This promotional material will also serve as a handout at events, to potential customers, and more. We welcome creative ideas and suggestions to maximize the versatility of this design and reach diverse target audiences effectively.

For a comprehensive overview of our services and to explore our design concepts, please visit https://quarrytidehosting.example. Quarrytide Hosting is poised to revolutionize the mining industry, and we look forward to partnering with you for success in the digital currency era.

```html
<!DOCTYPE html>
<html lang="en">
<head>
<meta charset="utf-8">
<title>Quarrytide Hosting – Flyer</title>
<link rel="stylesheet" href="https://fonts.googleapis.com/css2?family=Chakra+Petch:wght@500;600;700&family=Saira+Condensed:wght@600;700&family=Saira+Semi+Condensed:wght@600;700&family=Archivo:wght@400;500;600&display=swap">
<style>
:root{
  --blue:#3a4cf2;
  --blue-deep:#2f3fe0;
  --green:#1b9a3e;
  --ink:#1f1f2b;
  --muted:#4a4a58;
  --lavender:#e6e9fd;
  --mint:#e3f2e7;
  --page:#ececee;
  --paper:#ffffff;
  --badge:#f2e24a;
}
*{box-sizing:border-box;margin:0;padding:0}
html,body{width:1200px;height:2481px;overflow:hidden;background:var(--page)}
body{position:relative;font-family:"Archivo",Arial,sans-serif;color:var(--ink)}
.flyer-frame{position:absolute;left:40px;top:515px;width:1120px;height:1450px;box-shadow:0 10px 40px rgba(0,0,0,.18);background:var(--paper);overflow:hidden}
.flyer{position:absolute;left:0;top:0;width:977px;height:1265px;transform:scale(1.1464);transform-origin:0 0}
.abs{position:absolute}
.head{font-family:"Saira Semi Condensed",Arial,sans-serif;font-weight:700;text-transform:uppercase;line-height:1}
.cond{font-family:"Saira Condensed",Arial,sans-serif}

.brand{left:75px;top:80px;display:flex;align-items:center;gap:12px}
.brand-mark{width:42px;height:40px;background:var(--ink);border-radius:3px}
.brand-name{font-size:44px;color:var(--ink);letter-spacing:.5px}

.launch{left:75px;top:145px;font-size:24px;color:var(--blue);font-weight:600}

.hero{left:75px;top:188px;width:460px;height:224px;background:var(--lavender);border-radius:20px;padding:22px 0 0 21px}
.hero-lead{font-size:26px;line-height:26px;color:var(--ink);font-weight:600}
.hero-title{font-size:62px;color:var(--blue);margin-top:10px;letter-spacing:0}
.hero-title.big{font-size:88px;margin-top:-6px}

.art-top{left:575px;top:0;width:355px;height:440px;border-radius:0 0 30px 30px;background:linear-gradient(180deg,#f2f4ff 0%,#dfe3fb 60%,#d3e9f6 100%)}
.art-left{left:30px;top:460px;width:385px;height:320px;border-radius:30px;background:radial-gradient(ellipse at 50% 55%,#9fb3fb 0%,#d7defd 55%,#ffffff 85%)}

.standout{left:443px;top:466px;font-size:25px;line-height:26px;font-weight:600;color:var(--ink)}

.plan{top:528px;width:225px;height:287px;border-radius:16px;padding:12px 14px}
.plan.gpu{left:442px;background:var(--lavender)}
.plan.asic{left:680px;background:var(--mint)}
.plan-icon{width:50px;height:50px;border-radius:7px;display:flex;align-items:center;justify-content:center}
.gpu .plan-icon{background:var(--blue)}
.asic .plan-icon{background:var(--green)}
.plan-name{font-family:"Chakra Petch",Arial,sans-serif;font-weight:600;font-size:31px;margin-top:14px;line-height:1;white-space:nowrap}
.gpu .plan-name{color:var(--blue)}
.asic .plan-name{color:var(--green)}
.plan-price{font-family:"Chakra Petch",Arial,sans-serif;font-weight:600;font-size:29px;line-height:1;margin-top:4px}
.plan-price sup{font-size:15px;vertical-align:top}
.plan-unit{font-size:16px;font-weight:500;margin-top:2px}
.plan-list{list-style:none;margin-top:12px}
.plan-list li{position:relative;padding-left:18px;font-size:11.5px;line-height:13px;margin-bottom:9px}
.gpu .plan-list li{color:var(--blue)}
.asic .plan-list li{color:var(--green)}
.plan-list li::before{content:"";position:absolute;left:2px;top:2px;width:7px;height:4px;border-left:1.5px solid currentColor;border-bottom:1.5px solid currentColor;transform:rotate(-45deg)}

.company{left:75px;top:828px}
.eyebrow{font-size:21px;color:var(--blue);font-weight:600}
.solutions{font-size:33px;line-height:31px;font-weight:600;margin-top:6px}
.stat{left:75px;display:flex;gap:14px;align-items:flex-start}
.stat-num{font-family:"Chakra Petch",Arial,sans-serif;font-weight:700;font-size:31px;line-height:1}
.stat-text{font-size:16px;font-weight:500}
.stat.blue{top:942px;color:var(--blue)}
.stat.green{top:1004px;color:var(--green)}

.services{left:463px;top:836px;width:470px;list-style:none}
.services li{display:flex;gap:14px;margin-bottom:14px}
.svc-icon{width:18px;flex:none;padding-top:3px}
.svc-title{font-family:"Chakra Petch",Arial,sans-serif;font-weight:600;font-size:19px;line-height:22px;display:flex;align-items:center;gap:8px}
.svc-desc{font-size:12.5px;line-height:14px;color:var(--muted)}
.badge{font-family:"Archivo",Arial,sans-serif;font-size:6.5px;font-weight:500;padding:3px 9px;border-radius:8px;text-transform:uppercase}
.badge.yellow{background:var(--badge);color:var(--ink)}
.badge.green{background:var(--green);color:#fff}

.cta{left:75px;top:1088px;width:825px;height:82px;border-radius:14px;background:linear-gradient(90deg,var(--blue) 0%,var(--blue-deep) 100%);color:#fff}
.cta-lead{position:absolute;left:26px;top:17px;font-size:23px;line-height:25px;font-weight:600}
.contact{position:absolute;top:12px;white-space:nowrap}
.contact svg{display:block;margin-bottom:6px}
.contact-label{font-family:"Chakra Petch",Arial,sans-serif;font-size:18px;font-weight:600;line-height:1}
.contact-sub{font-size:10px;line-height:14px}

.site{left:0;top:1192px;width:977px;text-align:center;font-size:21px;letter-spacing:4px;color:var(--muted);font-weight:500}
</style>
</head>
<body>
<div class="flyer-frame">
<div class="flyer">

  <div class="abs art-top" role="img" aria-label="Isometric illustration of a data center with server racks, coins, cash, monitors and small workers, linked by a blue route showing facility features"></div>

  <div class="abs brand">
    <span class="brand-mark"></span>
    <span class="brand-name head cond">Quarrytide Hosting</span>
  </div>

  <p class="abs launch head">We are launch of our new company</p>

  <div class="abs hero">
    <p class="hero-lead head">A premier cohosting facility<br>and data center dedicated to</p>
    <p class="hero-title head cond">Cryptocurrency</p>
    <p class="hero-title big head cond">Miners</p>
  </div>

  <div class="abs art-left" role="img" aria-label="Isometric illustration of a large blue computer with server tower and small technicians"></div>

  <p class="abs standout head">Quarrytide Hosting stands out in<br>the industry by offering both</p>

  <div class="abs plan gpu">
    <div class="plan-icon"><svg width="30" height="20" viewBox="0 0 30 20"><rect x="1" y="3" width="28" height="14" rx="2" fill="none" stroke="#fff" stroke-width="2"/><circle cx="11" cy="10" r="4" fill="none" stroke="#fff" stroke-width="2"/><circle cx="20" cy="10" r="4" fill="none" stroke="#fff" stroke-width="2"/></svg></div>
    <p class="plan-name">GPU Hosting</p>
    <p class="plan-price"><sup>$</sup>0.09</p>
    <p class="plan-unit">kilowatt-hour</p>
    <ul class="plan-list">
      <li>One Time Setup Fee of<br>$50 Per GPU Rig</li>
      <li>All-In $0.09 Per Kilowatt-Hour,<br>No Additional Fees</li>
      <li>Remotely Monitor &amp; Access<br>Your Equipment 24/7</li>
    </ul>
  </div>

  <div class="abs plan asic">
    <div class="plan-icon"><svg width="30" height="20" viewBox="0 0 30 20"><rect x="1" y="3" width="28" height="14" rx="2" fill="none" stroke="#fff" stroke-width="2"/><circle cx="11" cy="10" r="4" fill="none" stroke="#fff" stroke-width="2"/><circle cx="20" cy="10" r="4" fill="none" stroke="#fff" stroke-width="2"/></svg></div>
    <p class="plan-name">ASIC Hosting</p>
    <p class="plan-price"><sup>$</sup>0.08</p>
    <p class="plan-unit">kilowatt-hour</p>
    <ul class="plan-list">
      <li>One Time Setup Fee of $50<br>Per ASIC Unit</li>
      <li>All-In $0.08 Per Kilowatt-Hour,<br>No Additional Fees</li>
      <li>Remotely Monitor &amp; Access<br>Your Equipment 24/7</li>
    </ul>
  </div>

  <div class="abs company">
    <p class="eyebrow head">Company</p>
    <p class="solutions head">Real solutions for<br>real applications</p>
  </div>

  <div class="abs stat blue">
    <svg width="36" height="34" viewBox="0 0 36 34" fill="none" stroke="currentColor" stroke-width="2.2"><rect x="2" y="12" width="12" height="20" rx="2"/><rect x="20" y="2" width="14" height="30" rx="2"/><line x1="2" y1="22" x2="14" y2="22"/><line x1="20" y1="12" x2="34" y2="12"/><line x1="20" y1="22" x2="34" y2="22"/></svg>
    <div><p class="stat-num">4,000,000+</p><p class="stat-text">watts available for hosting</p></div>
  </div>

  <div class="abs stat green">
    <svg width="36" height="36" viewBox="0 0 36 36" fill="none" stroke="currentColor" stroke-width="2.2"><circle cx="17" cy="17" r="14"/><ellipse cx="17" cy="17" rx="6" ry="14"/><line x1="3" y1="17" x2="31" y2="17"/><circle cx="30" cy="30" r="4" fill="#fff"/></svg>
    <div><p class="stat-num">2,000,000+</p><p class="stat-text">watts of green energy being produced</p></div>
  </div>

  <ul class="abs services">
    <li>
      <svg class="svc-icon" viewBox="0 0 18 18"><rect x="3" y="4" width="12" height="10" rx="2" transform="rotate(-35 9 9)" fill="var(--blue)"/></svg>
      <div><p class="svc-title">GPU Hosting</p><p class="svc-desc">Begin your GPU Hosting journey with rates starting at $0.09 kWh</p></div>
    </li>
    <li>
      <svg class="svc-icon" viewBox="0 0 18 18" fill="none" stroke="var(--blue)" stroke-width="1.8"><rect x="4" y="4" width="10" height="10" rx="1.5"/><path d="M7 1v3M11 1v3M7 14v3M11 14v3M1 7h3M1 11h3M14 7h3M14 11h3"/></svg>
      <div><p class="svc-title">ASIC Hosting <span class="badge yellow">Most popular</span></p><p class="svc-desc">Get your ASICs directly from us or send yours in today, starting at an<br>all-in rate of $0.08 kWh</p></div>
    </li>
    <li>
      <svg class="svc-icon" viewBox="0 0 18 18" fill="var(--blue)"><path d="M2 2l5 3h4l5-3-3 5v4l3 5-5-3H7l-5 3 3-5V7z"/></svg>
      <div><p class="svc-title">Mining Hardware</p><p class="svc-desc">Begin your GPU Hosting journey with rates starting at $0.09 kWh</p></div>
    </li>
    <li>
      <svg class="svc-icon" viewBox="0 0 18 18" fill="none" stroke="var(--blue)" stroke-width="1.8"><rect x="3" y="1" width="12" height="16" rx="2"/><path d="M6 6h6M6 10h6"/></svg>
      <div><p class="svc-title">Crypto Consulting <span class="badge green">Most popular</span></p><p class="svc-desc">Enjoy White Glove Services for setup, insurance, and tax consulting.</p></div>
    </li>
  </ul>

  <div class="abs cta">
    <p class="cta-lead head">Your mining success<br>story begins here</p>
    <div class="contact" style="left:385px">
      <svg width="22" height="20" viewBox="0 0 22 20" fill="none" stroke="#fff" stroke-width="1.8"><path d="M3 2h4l2 5-2.5 1.5a11 11 0 005 5L13 11l5 2v4a2 2 0 01-2 2A15 15 0 011 4a2 2 0 012-2z"/></svg>
      <p class="contact-label">Chat us</p><p class="contact-sub">Live Chat</p>
    </div>
    <div class="contact" style="left:478px">
      <svg width="22" height="20" viewBox="0 0 22 20" fill="none" stroke="#fff" stroke-width="1.8"><rect x="1" y="3" width="20" height="14" rx="1.5"/><path d="M1 4l10 7 10-7"/></svg>
      <p class="contact-label">Live Chat</p><p class="contact-sub">hello@quarrytidehosting.example</p>
    </div>
    <div class="contact" style="left:668px">
      <svg width="22" height="20" viewBox="0 0 22 20" fill="none" stroke="#fff" stroke-width="1.8"><path d="M9 3H2v15h15v-7"/><path d="M13 2h7v7M20 2L10 12"/></svg>
      <p class="contact-label">Schedule 1-On-1</p><p class="contact-sub">Interact With Us</p>
    </div>
  </div>

  <p class="abs site">www.quarrytidehosting.example</p>

</div>
</div>
</body>
</html>
```